Business Card for a Floral & Decorating Business

I would like to take my current logo and create a better business card. I am looking for elegance as I am a florist and event decorator. My logo has multiple colour options. I like colours like green, purple, pink and orange, I think I would like a white card, open to black back ground. I want it to feel elegant and romantic. I like metallic lettering that maybe is indented in the paper, I also like glossy paper. I have a full logo already as well as a badge. I have attached both in multiple colours.m
Updates

Need extra days to review

Target Market(s)

Weddings, special events, floral customers

Industry/Entity Type

Floral and decorating

Contact Information for Business Card

Phone number, email, instagram, facebook, title, name, logo

Font styles to use
Script

Requirements
Nice to have
• Elegant

```html
<!DOCTYPE html>
<html lang="en">
<head>
<meta charset="utf-8">
<title>Petal &amp; Vine Studio — Business Card</title>
<link href="https://fonts.googleapis.com/css2?family=Allura&family=Cormorant+Garamond:wght@400;500&family=Montserrat:wght@500;600&display=swap" rel="stylesheet">
<style>
  :root {
    --page: #ffffff;
    --card: #e8b8a8;
    --ink: #2c2e44;
    --white: #ffffff;
    --bloom-deep: #a8445a;
    --bloom-mid: #d98a7c;
    --bloom-light: #f2c6b0;
    --bloom-peach: #e6a57a;
    --leaf: #5d7886;
  }
  * { box-sizing: border-box; margin: 0; padding: 0; }
  html, body { width: 687px; height: 1200px; overflow: hidden; background: var(--page); }
  .sheet { position: relative; width: 687px; height: 1200px; }

  .card {
    position: absolute; left: 63px; width: 560px; height: 320px;
    background: var(--card); overflow: hidden;
    box-shadow: 0 3px 8px rgba(0,0,0,.18);
  }
  .card--front { top: 230px; }
  .card--back { top: 630px; }

  .bloom {
    position: absolute;
    background:
      radial-gradient(circle at 55% 40%, var(--bloom-deep) 0 18%, transparent 42%),
      radial-gradient(circle at 35% 60%, var(--bloom-peach) 0 22%, transparent 50%),
      radial-gradient(circle at 60% 55%, var(--bloom-mid) 0 30%, transparent 62%),
      radial-gradient(circle at 50% 50%, var(--bloom-light) 0 40%, transparent 72%);
    border-radius: 50%;
    opacity: .92;
  }
  .sprig {
    position: absolute; border-radius: 50%;
    background: radial-gradient(ellipse at center, rgba(93,120,134,.55) 0 30%, rgba(242,198,176,.4) 55%, transparent 75%);
  }
  .brush {
    position: absolute;
    background: linear-gradient(100deg, rgba(255,255,255,0) 0%, rgba(255,255,255,.95) 35%, rgba(255,255,255,.9) 70%, rgba(255,255,255,0) 100%);
  }

  .mark {
    position: absolute; display: flex; flex-direction: column; align-items: center;
    color: var(--white);
    font-family: "Cormorant Garamond", serif; font-weight: 500;
    letter-spacing: .18em; text-transform: uppercase; text-align: center;
  }
  .mark__circle { border: 1.5px solid var(--white); border-radius: 50%; }
  .card--front .mark { left: 180px; top: 88px; width: 200px; font-size: 17px; }
  .card--front .mark__circle { width: 96px; height: 96px; margin-bottom: 16px; }
  .card--back .mark { left: 24px; top: 108px; width: 160px; font-size: 12px; }
  .card--back .mark__circle { width: 64px; height: 64px; margin-bottom: 12px; }

  .divider { position: absolute; left: 206px; top: 53px; width: 1px; height: 214px; background: var(--white); }

  .identity { position: absolute; left: 226px; top: 36px; color: var(--white); }
  .identity__name { font-family: "Allura", cursive; font-size: 38px; line-height: 1; letter-spacing: .02em; }
  .identity__title {
    margin: 4px 0 0 52px; font-family: "Cormorant Garamond", serif;
    font-size: 7px; letter-spacing: .3em; text-transform: uppercase;
  }

  .contact { position: absolute; left: 231px; top: 112px; list-style: none; color: var(--ink); font-family: "Montserrat", sans-serif; }
  .contact__item { display: flex; align-items: center; gap: 10px; height: 33px; }
  .contact__item svg { width: 14px; height: 14px; flex: none; }
  .contact__phone { font-size: 18px; font-weight: 600; letter-spacing: .02em; }
  .contact__text { font-size: 13px; font-weight: 500; }
</style>
</head>
<body>
<main class="sheet">

  <section class="card card--front" aria-label="Business card front">
    <div class="brush" role="img" aria-label="White brush stroke" style="left:-10px;top:0;width:80px;height:38px;transform:rotate(-12deg);"></div>
    <div class="brush" role="img" aria-label="White brush stroke" style="left:500px;top:275px;width:70px;height:40px;transform:rotate(-14deg);"></div>
    <div class="bloom" role="img" aria-label="Watercolour peony cluster" style="left:455px;top:-30px;width:140px;height:130px;"></div>
    <div class="sprig" role="img" aria-label="Watercolour leaves and buds" style="left:500px;top:90px;width:70px;height:100px;"></div>
    <div class="bloom" role="img" aria-label="Watercolour peony cluster" style="left:-35px;top:215px;width:150px;height:130px;"></div>
    <div class="sprig" role="img" aria-label="Watercolour leaves and buds" style="left:-10px;top:165px;width:60px;height:70px;"></div>
    <div class="sprig" role="img" aria-label="Watercolour blossom sprig" style="left:100px;top:280px;width:100px;height:40px;"></div>
    <div class="mark">
      <span class="mark__circle"></span>
      <span>Petal &amp; Vine Studio</span>
    </div>
  </section>

  <section class="card card--back" aria-label="Business card back">
    <div class="brush" role="img" aria-label="White brush stroke" style="left:-10px;top:0;width:80px;height:40px;transform:rotate(-12deg);"></div>
    <div class="brush" role="img" aria-label="White brush stroke" style="left:505px;top:280px;width:65px;height:36px;transform:rotate(-14deg);"></div>
    <div class="bloom" role="img" aria-label="Watercolour peony cluster" style="left:455px;top:-30px;width:140px;height:130px;"></div>
    <div class="sprig" role="img" aria-label="Watercolour leaves and buds" style="left:500px;top:90px;width:70px;height:100px;"></div>
    <div class="sprig" role="img" aria-label="Watercolour blossom sprig" style="left:390px;top:-5px;width:90px;height:35px;"></div>
    <div class="bloom" role="img" aria-label="Watercolour peony cluster" style="left:-30px;top:235px;width:130px;height:110px;"></div>
    <div class="sprig" role="img" aria-label="Watercolour leaves and blossom sprig" style="left:70px;top:255px;width:130px;height:60px;"></div>

    <div class="mark">
      <span class="mark__circle"></span>
      <span>Petal &amp; Vine Studio</span>
    </div>

    <span class="divider"></span>

    <div class="identity">
      <p class="identity__name">marlowe ainsley</p>
      <p class="identity__title">Petal &amp; Vine Studio.</p>
    </div>

    <ul class="contact">
      <li class="contact__item">
        <svg viewBox="0 0 16 16" aria-hidden="true"><path fill="var(--white)" d="M4 1.5l2.2 3-1.3 1.6c.9 1.9 2.3 3.3 4.2 4.2l1.6-1.3 3 2.2-1.2 2.6C7 13.5 2.5 9 1.4 2.7z"/></svg>
        <span class="contact__phone">555-0142-678</span>
      </li>
      <li class="contact__item">
        <svg viewBox="0 0 16 16" aria-hidden="true"><rect x="1" y="3.5" width="14" height="9" fill="var(--white)"/><path d="M1.5 4l6.5 5 6.5-5" fill="none" stroke="var(--card)" stroke-width="1"/></svg>
        <span class="contact__text">hello@petalandvine.com</span>
      </li>
      <li class="contact__item">
        <svg viewBox="0 0 16 16" aria-hidden="true"><circle cx="8" cy="8" r="6.5" fill="none" stroke="var(--white)" stroke-width="1.5"/><path d="M1.5 8h13M8 1.5c-3 3-3 10 0 13M8 1.5c3 3 3 10 0 13" fill="none" stroke="var(--white)" stroke-width="1.2"/></svg>
        <span class="contact__text">www.petalandvine.com</span>
      </li>
    </ul>
  </section>

</main>
</body>
</html>
```